QuarryNest - Webstartup looking for some style

QuarryNest is a cloud based web application that allows construction sub-contractors to create and manage bids. Generally, these contractors will contact subcontractors to have them do specific parts of a larger construction project. This would be used by various subcontractors including woodwork (cabinetry), electricians, masons, etc...

Nearly all competitors are clients applications that have to be installed on the computer and are very expensive. This is a much lower cost alternative.

The business is just beginning and we want people to view us as a fresh alternative to companies that have been around for a long time and are starting to look a little dated.

We would like our logo included on the card (see attached). We have been using the circular 'qn' emblem seperately from the complete logo in various areas of the website. We lean towards a professional and clean look, with a tendancy more towards modern.

We want to differentiate ourselves from our competition which tend to be dated, complicated and less graphical.

(We are currently designing our public website as well - but don't have any designs yet)

Industry/Entity Type

Construction

Requirements
Must have
• Circular 'qn' emblem from logo. Probably entire logo, but not necessarily.

Should have reference to website: www.quarrynest-demo.net

The Url should be all lowercase (www.quarrynest-demo.net)
Should not have
• we do not want to list a phone number or email address on the cards. we want people to go to the actual website. we haven't decided if we want names printed on the business cards.

```html
<!DOCTYPE html>
<html lang="en">
<head>
<meta charset="utf-8">
<title>QuarryNest Business Cards</title>
<link rel="stylesheet" href="https://fonts.googleapis.com/css2?family=Questrial&family=Roboto+Condensed:wght@700&display=swap">
<style>
  :root {
    --stage: #e9edf1;
    --brand-blue: #1f86c8;
    --brand-blue-light: #5bbde6;
    --brand-orange: #f39a26;
    --brand-orange-light: #fbc56c;
    --ink: #2a2a2a;
    --paper: #ffffff;
    --paper-shade: #e6e6e6;
  }
  * { margin: 0; padding: 0; box-sizing: border-box; }
  html, body {
    width: 1200px; height: 1200px; overflow: hidden;
    background: var(--stage);
  }
  .stage {
    width: 1200px; height: 1200px;
    display: flex; flex-direction: column; align-items: center; justify-content: center;
    gap: 60px;
  }
  .card {
    position: relative;
    width: 900px; height: 500px;
    overflow: hidden;
    box-shadow: 0 10px 30px rgba(0,0,0,0.18);
  }

  /* Front */
  .card--front {
    background: radial-gradient(ellipse at 50% 30%, var(--paper) 0%, #f4f4f4 60%, var(--paper-shade) 100%);
  }
  .front-brand {
    position: absolute; left: 0; right: 0; top: 70px;
    display: flex; flex-direction: column; align-items: center;
  }
  .brand-mark {
    width: 96px; height: 96px; border-radius: 50%;
    background: var(--brand-blue);
    margin-bottom: 18px;
  }
  .brand-name {
    font-family: "Questrial", sans-serif;
    font-size: 104px; line-height: 1;
    color: var(--brand-blue);
    letter-spacing: -1px;
  }
  .tagline {
    font-family: "Roboto Condensed", sans-serif;
    font-weight: 700;
    font-size: 28px;
    color: var(--ink);
    margin-top: 10px;
    letter-spacing: -0.3px;
  }
  .band { position: absolute; }
  .band--orange { right: 0; width: 320px; top: 350px; height: 108px; background: var(--brand-orange); }
  .band--blue { left: 0; width: 580px; top: 394px; height: 64px; background: var(--brand-blue); }
  .front-url {
    position: absolute; left: 160px; top: 394px; height: 64px;
    display: flex; align-items: center;
    font-family: "Questrial", sans-serif;
    font-size: 44px; color: var(--paper);
    letter-spacing: 1px;
  }

  /* Back */
  .card--back {
    background:
      radial-gradient(ellipse at 55% 0%, var(--brand-orange-light) 0%, rgba(251,197,108,0) 55%),
      linear-gradient(135deg, var(--brand-orange) 0%, #ee8d1c 100%);
  }
  .back-band {
    position: absolute; left: 0; top: 0; bottom: 0; width: 170px;
    background: linear-gradient(180deg, var(--brand-blue-light) 0%, var(--brand-blue) 60%);
  }
  .back-ring {
    position: absolute; left: 250px; top: 50px;
    width: 220px; height: 220px; border-radius: 50%;
    border: 32px solid var(--paper);
  }
  .back-info {
    position: absolute; right: 60px; bottom: 50px;
    display: flex; flex-direction: column; align-items: flex-end;
    color: var(--paper);
  }
  .back-info .brand-name { color: var(--paper); font-size: 78px; }
  .back-info .tagline { color: var(--paper); font-size: 21px; margin-top: 4px; }
  .back-url {
    font-family: "Questrial", sans-serif;
    font-size: 38px; margin-top: 14px; letter-spacing: 1px;
  }
</style>
</head>
<body>
  <main class="stage">
    <section class="card card--front" aria-label="Business card front">
      <div class="front-brand">
        <div class="brand-mark" aria-hidden="true"></div>
        <h1 class="brand-name">QuarryNest</h1>
        <p class="tagline">Empowering Subcontractor Proposals</p>
      </div>
      <div class="band band--orange"></div>
      <div class="band band--blue"></div>
      <p class="front-url">www.quarrynest-demo.net</p>
    </section>

    <section class="card card--back" aria-label="Business card back">
      <div class="back-band"></div>
      <div class="back-ring" aria-hidden="true"></div>
      <div class="back-info">
        <h2 class="brand-name">QuarryNest</h2>
        <p class="tagline">Empowering Subcontractor Proposals</p>
        <p class="back-url">www.quarrynest-demo.net</p>
      </div>
    </section>
  </main>
</body>
</html>
```